Book Cover for my Autobiography

I would like to see a CONCEPT of the Front Cover as per the following.
a) Take me out of the FILE NAMED=1-MAIN.jpg
b) I want my Wife "Watching over me" - behind me - in the SHADOWS. You can take her image for the concept from the FILE NAMED=2-Wife Watching over me.jpg.
c) This based on the old saying that "Behind every Good Man....is a Woman".  So that's what I want to convert because my wife has always been in the background, in the "Shadows" - always supporting and encouraging me in whatever I do.
d) This book is purely for my children, wife, siblings, relatives and Friends.
e) the Book Cover has to be designed FLAT & RECTANGULAR - like the sample leather cover.  i.e. NOT viewed from an Angle.
f) The Book Title is "Salt in the Orchard"
g) I have no pre-conceived ideas of design or colours or styling etc.  I want a PROFESSIONAL DESIGNER to come up with the best Overall Design that conveys the "Supportive Wife" always behind me and supporting me - While I am out front as the subject.
h) When the Design is accepted, I will provide the main photo of my wife without my son in front of her that I want to use - and one me without my wife's arms around me.  But if you can do that too (i.e. reconstruct my Wife's Burgundy top & and remove her arms from around me-then even better because I don't have to hire another graphic designer to do that for me).
My name is "Tomas Brenhoek" so the author of the autobiography needs to be SOMEWHERE.
h) And last, please just put some text - maybe 2 sentences for the summary of the story like many Autobiographies do. eg.
"My story of how ....Lorem ipsum dolor sit amet, consectetur adipiscing elit, sed do eiusmod tempor incididunt. Integer vitae justo eget magna fermentum iaculis eu non. Aliquam eleifend".

I forgot to mention that this Book Cover is actually going on an eBOOK - not a Printed Book.
It's just for Family and Friends.

```html
<!DOCTYPE html>
<html lang="en">
<head>
<meta charset="utf-8">
<title>Salt in the Orchard — eBook Cover</title>
<link rel="stylesheet" href="https://fonts.googleapis.com/css2?family=Montserrat:wght@400;500;700;800&display=swap">
<style>
  :root {
    --backdrop: #e3e4e6;
    --cover-top: #0b1720;
    --cover-mid: #0c1b28;
    --cover-bottom: #070f17;
    --wife-tone-light: #2a4258;
    --wife-tone-dark: #132434;
    --hair: #141a20;
    --skin: #9a6552;
    --skin-shade: #5c3e38;
    --shirt: #1f3a64;
    --shirt-dark: #12233d;
    --collar: #a8393a;
    --gold: #c9b08a;
    --white: #ffffff;
    --rule: #55606b;
    --body-text: #d9dde1;
  }
  * { margin: 0; padding: 0; box-sizing: border-box; }
  html, body {
    width: 1200px;
    height: 606px;
    overflow: hidden;
    background: var(--backdrop);
    font-family: "Montserrat", sans-serif;
  }
  .cover {
    position: absolute;
    left: 413px;
    top: 23px;
    width: 374px;
    height: 560px;
    background: linear-gradient(180deg, var(--cover-top) 0%, var(--cover-mid) 55%, var(--cover-bottom) 100%);
    box-shadow: 0 10px 28px rgba(0, 0, 0, 0.28);
    overflow: hidden;
  }

  /* Portrait zones */
  .portrait-wife {
    position: absolute;
    left: 10px;
    top: 150px;
    width: 185px;
    height: 290px;
    border-radius: 46% 46% 20% 20% / 36% 36% 12% 12%;
    background: radial-gradient(ellipse 60% 50% at 50% 48%, var(--wife-tone-light) 0%, var(--wife-tone-dark) 70%, rgba(12, 27, 40, 0) 100%);
    opacity: 0.75;
    filter: blur(3px);
  }
  .portrait-author {
    position: absolute;
    left: 72px;
    top: 122px;
    width: 302px;
    height: 350px;
    border-radius: 48% 48% 6% 6% / 40% 40% 6% 6%;
    background:
      radial-gradient(ellipse 34% 30% at 62% 52%, var(--skin) 0%, var(--skin-shade) 70%, rgba(92, 62, 56, 0) 100%),
      linear-gradient(180deg, var(--hair) 0%, var(--hair) 22%, var(--skin-shade) 42%, var(--skin-shade) 62%, var(--collar) 72%, var(--shirt) 80%, var(--shirt-dark) 100%);
    filter: blur(2px);
  }
  .portrait-fade {
    position: absolute;
    left: 0;
    top: 400px;
    width: 100%;
    height: 160px;
    background: linear-gradient(180deg, rgba(7, 15, 23, 0) 0%, rgba(7, 15, 23, 0.55) 45%, var(--cover-bottom) 85%);
  }

  /* Title */
  .title-kicker {
    position: absolute;
    top: 33px;
    left: 0;
    width: 100%;
    text-align: center;
    color: var(--gold);
    font-weight: 400;
    font-size: 24px;
    letter-spacing: 0.4em;
    padding-left: 0.4em;
    line-height: 1;
  }
  .title-main {
    position: absolute;
    top: 62px;
    left: 0;
    width: 100%;
    text-align: center;
    color: var(--white);
    font-weight: 800;
    font-size: 64px;
    letter-spacing: -0.03em;
    line-height: 1;
  }

  /* Author */
  .author-block {
    position: absolute;
    left: 0;
    top: 474px;
    width: 100%;
    text-align: center;
  }
  .author-label {
    color: var(--gold);
    font-size: 8.5px;
    font-weight: 400;
    letter-spacing: 0.34em;
    padding-left: 0.34em;
  }
  .author-name {
    margin-top: 8px;
    color: var(--white);
    font-size: 14px;
    font-weight: 700;
    letter-spacing: 0.42em;
    padding-left: 0.42em;
  }
  .author-rule {
    width: 226px;
    height: 1px;
    margin: 7px auto 0;
    background: var(--rule);
  }
  .summary {
    width: 300px;
    margin: 5px auto 0;
    color: var(--body-text);
    font-size: 6px;
    line-height: 1.75;
    font-weight: 400;
  }
</style>
</head>
<body>
  <main class="cover">
    <div class="portrait-wife" role="img" aria-label="Photograph of the author's wife, dimly lit in the shadows behind him"></div>
    <div class="portrait-author" role="img" aria-label="Photograph of the author smiling, in a navy sweater over a red collared shirt"></div>
    <div class="portrait-fade"></div>

    <p class="title-kicker">SALT IN THE</p>
    <h1 class="title-main">ORCHARD</h1>

    <section class="author-block">
      <p class="author-label">AUTHOR OF THE AUTOBIOGRAPHY</p>
      <p class="author-name">TOMAS BRENHOEK</p>
      <div class="author-rule"></div>
      <p class="summary">My story of how ....Lorem ipsum dolor sit amet, consectetur adipiscing elit, sed do eiusmod tempor incididunt. Integer vitae justo eget magna fermentum iaculis eu non. Aliquam eleifend</p>
    </section>
  </main>
</body>
</html>
```